Documentary Movie Needs a Poster

We need a poster/lobby card for a documentary film made by six filmmakers. Lobby card needs to list name of sponsor, names of filmmakers and (if feasible, but not required) image frames from each of the six sections of the film.

Text should be very readable. OK to have all caps text or upper/lower.

Design comps are OK, these do not need to be print-ready final images.

Target Market(s)

well educated documentary filmgoers

Industry/Entity Type

Movie

Requirements
Must have
• Must contain the following text (please use helvetica neue or similar font).

Please use the following sponsor name:

The
Marlowe Institute for Cinema
presents

Please use the following filmmaker names:

Theodore Pelusky
Robert Nash
Frederick Tamworth
Harold E. F. Pratt
Vincent Lorimer
Danny Frost

Please use the 6 images in archive/zip to create the card.

You can also do text-only versions of the card (no images).

Card needs to be 2:1 aspect ratio (2000px wide x 1000 pixels high)

Names of filmmakers should each be same size (no filmmaker has visual priority over the other).

Colors for text, lines and other design elements should be RED, BLACK and/or WHITE.

Feel free to crop images if you need to.

```html
<!DOCTYPE html>
<html lang="en">
<head>
<meta charset="utf-8">
<title>The Marlowe Institute for Cinema presents</title>
<link href="https://fonts.googleapis.com/css2?family=Arimo:wght@400&display=swap" rel="stylesheet">
<style>
  :root {
    --ink: #000000;
    --red: #c8102e;
    --paper: #ffffff;
    --edge: #d4d4d4;
    --guide: #e4e4e4;
    --sprocket: #c9c9c9;
  }
  * { margin: 0; padding: 0; box-sizing: border-box; }
  html, body { width: 1200px; height: 599px; overflow: hidden; background: var(--paper); }
  .card {
    position: relative;
    width: 1200px;
    height: 599px;
    background: var(--paper);
    border: 1px solid var(--edge);
    font-family: "Arimo", "Helvetica Neue", Arial, sans-serif;
    overflow: hidden;
  }
  .guides { position: absolute; inset: 0; }
  .sponsor { position: absolute; left: 55px; top: 44px; color: var(--ink); }
  .sponsor-the { font-size: 19px; line-height: 22px; letter-spacing: 0.5px; }
  .sponsor-name { font-size: 44px; line-height: 52px; letter-spacing: 0.5px; margin-top: 4px; }
  .presents {
    position: absolute;
    left: 370px;
    top: 215px;
    transform: rotate(-90deg);
    transform-origin: left top;
    color: var(--red);
    font-size: 36px;
    line-height: 40px;
  }
  .reel { position: absolute; }
  .reel-strip { position: absolute; left: 0; top: 0; width: 36px; height: 150px; }
  .reel-frame {
    position: absolute;
    left: 36px;
    top: 0;
    width: 238px;
    height: 151px;
    border: 2px solid var(--ink);
  }
  .frame-road { background: linear-gradient(180deg, #c9ccd0 0%, #a9aaa5 45%, #8b8478 100%); }
  .frame-rooftop { background: linear-gradient(180deg, #b9bcc0 0%, #b69d78 45%, #6f6450 100%); }
  .frame-crowd { background: linear-gradient(180deg, #dfe3e6 0%, #9f8b6e 45%, #4d4a3b 100%); }
  .frame-wreck { background: linear-gradient(180deg, #e8e4dc 0%, #cdbb9c 50%, #a88f6b 100%); }
  .frame-soldier { background: linear-gradient(180deg, #d8d8d8 0%, #8e8e8e 50%, #3e3e3e 100%); }
  .frame-rally { background: linear-gradient(180deg, #3f7fc2 0%, #8fb2d6 50%, #3a3436 100%); }
  .reel-name {
    position: absolute;
    left: 32px;
    top: 166px;
    color: var(--red);
    font-size: 19px;
    line-height: 22px;
    white-space: nowrap;
  }
</style>
</head>
<body>
<div class="card">
  <svg class="guides" width="1200" height="599" viewBox="0 0 1200 599" aria-hidden="true">
    <g stroke="var(--guide)" stroke-width="2" fill="none">
      <line x1="0" y1="214" x2="1200" y2="318"/>
      <line x1="0" y1="305" x2="1200" y2="599"/>
      <line x1="640" y1="450" x2="880" y2="599"/>
    </g>
  </svg>

  <div class="sponsor">
    <div class="sponsor-the">THE</div>
    <div class="sponsor-name">MARLOWE<br>INSTITUTE<br>FOR CINEMA</div>
  </div>
  <div class="presents">presents</div>

  <svg width="0" height="0" style="position:absolute" aria-hidden="true">
    <defs>
      <symbol id="sprocket" viewBox="0 0 36 150">
        <rect x="0" y="0" width="36" height="150" fill="var(--sprocket)"/>
        <g fill="var(--paper)">
          <rect x="8" y="6" width="20" height="9"/>
          <rect x="8" y="23" width="20" height="9"/>
          <rect x="8" y="40" width="20" height="9"/>
          <rect x="8" y="57" width="20" height="9"/>
          <rect x="8" y="74" width="20" height="9"/>
          <rect x="8" y="91" width="20" height="9"/>
          <rect x="8" y="108" width="20" height="9"/>
          <rect x="8" y="125" width="20" height="9"/>
          <rect x="8" y="142" width="20" height="8"/>
        </g>
      </symbol>
    </defs>
  </svg>

  <div class="reel" style="left:604px; top:92px;">
    <svg class="reel-strip" aria-hidden="true"><use href="#sprocket"/></svg>
    <div class="reel-frame frame-road" role="img" aria-label="Film still: soldier kneeling on a desert road"></div>
    <div class="reel-name">Robert Nash</div>
  </div>

  <div class="reel" style="left:890px; top:92px;">
    <svg class="reel-strip" aria-hidden="true"><use href="#sprocket"/></svg>
    <div class="reel-frame frame-rooftop" role="img" aria-label="Film still: soldiers on a rooftop above a smoking city"></div>
    <div class="reel-name">Frederick Tamworth</div>
  </div>

  <div class="reel" style="left:32px; top:330px;">
    <svg class="reel-strip" aria-hidden="true"><use href="#sprocket"/></svg>
    <div class="reel-frame frame-crowd" role="img" aria-label="Film still: crowd of armed fighters raising rifles"></div>
    <div class="reel-name">Harold E. F. Pratt</div>
  </div>

  <div class="reel" style="left:318px; top:330px;">
    <svg class="reel-strip" aria-hidden="true"><use href="#sprocket"/></svg>
    <div class="reel-frame frame-wreck" role="img" aria-label="Film still: destroyed armoured vehicle in the sand"></div>
    <div class="reel-name">Theodore Pelusky</div>
  </div>

  <div class="reel" style="left:604px; top:330px;">
    <svg class="reel-strip" aria-hidden="true"><use href="#sprocket"/></svg>
    <div class="reel-frame frame-soldier" role="img" aria-label="Film still: black and white photo of a resting soldier among rubble"></div>
    <div class="reel-name" style="top:164px;">Vincent Lorimer</div>
  </div>

  <div class="reel" style="left:890px; top:330px;">
    <svg class="reel-strip" aria-hidden="true"><use href="#sprocket"/></svg>
    <div class="reel-frame frame-rally" role="img" aria-label="Film still: anti-war rally with placards before a domed capitol"></div>
    <div class="reel-name" style="top:164px;">Danny Frost</div>
  </div>
</div>
</body>
</html>
```